Bramwell HVAC Service LLC Business Card

We just got a design created by one of your designers for a logo and now would like help with a business card design. The information to be included on the card is as follows:
Bramwell HVAC Service LLC (I will attach logo design)
P.O. Box 482
Dunmore, CO 80634
(970) 347-6159
Lonnie Tadwick
I might include an e-mail address, but I'm not sure yet.
Target Market(s)
Customers needing service or repairs done on their heating and air conditioning systems.
Industry/Entity Type
Business
Contact Information for Business Card
P.O. Box 482
Dunmore, CO 80634
(970) 347-6159
Lonnie Tadwick

```html
<!DOCTYPE html>
<html lang="en">
<head>
<meta charset="utf-8">
<title>Bramwell HVAC Service LLC – Business Card</title>
<link rel="stylesheet" href="https://fonts.googleapis.com/css2?family=Arimo:wght@400;700&display=swap">
<style>
  :root {
    --bg: #eceef0;
    --card: #f7f7f7;
    --brand-blue: #0d4f9e;
    --brand-navy: #1e3c72;
    --brand-red: #d8262f;
    --text-grey: #5a5f66;
    --social-grey: #7d97b3;
    --white: #ffffff;
  }
  * { box-sizing: border-box; margin: 0; padding: 0; }
  html, body { width: 1200px; height: 900px; overflow: hidden; }
  body {
    background: var(--bg);
    font-family: "Arimo", Arial, sans-serif;
    display: flex;
    align-items: center;
    justify-content: center;
    gap: 40px;
  }
  .card {
    width: 500px;
    height: 286px;
    position: relative;
    box-shadow: 0 6px 18px rgba(0,0,0,.12);
  }
  /* Front */
  .card-front { background: var(--card); padding: 34px 36px; }
  .brand {
    display: flex; align-items: center; gap: 12px;
  }
  .brand-dot {
    width: 38px; height: 38px; border-radius: 50%;
    background: var(--brand-navy);
  }
  .brand-name {
    font-weight: 700; font-size: 26px; letter-spacing: .5px;
    color: var(--brand-red); text-transform: uppercase;
  }
  .social {
    position: absolute; top: 38px; right: 36px;
    display: flex; gap: 5px;
  }
  .social span {
    width: 16px; height: 16px; background: var(--social-grey); border-radius: 2px;
  }
  .person { margin-top: 44px; }
  .person-name {
    color: var(--brand-red); font-weight: 700; font-size: 16px;
    text-transform: uppercase; letter-spacing: .5px;
  }
  .person-role { color: var(--text-grey); font-size: 12px; margin-top: 3px; }
  .contact { margin-top: 12px; list-style: none; }
  .contact li {
    display: flex; align-items: center; gap: 8px;
    color: var(--text-grey); font-size: 12px; line-height: 20px;
  }
  .contact svg { width: 11px; height: 11px; fill: var(--brand-red); }
  .address { color: var(--text-grey); font-size: 12px; margin-top: 10px; }

  /* Back */
  .card-back {
    background: var(--brand-blue); overflow: hidden;
  }
  .back-mark {
    position: absolute; left: 70px; top: 20px;
    width: 240px; height: 240px; border-radius: 50%;
    background: rgba(10, 40, 110, .35);
  }
  .back-title {
    position: absolute; right: 36px; top: 150px; text-align: right;
    color: var(--white); font-weight: 700; text-transform: uppercase;
  }
  .back-title .line1 { font-size: 28px; letter-spacing: 1px; }
  .back-title .line2 {
    font-size: 18px; letter-spacing: 1px;
    display: flex; align-items: center; justify-content: flex-end; gap: 10px;
  }
  .back-title .rule { width: 120px; height: 2px; background: var(--white); }
</style>
</head>
<body>
  <section class="card card-front" aria-label="Business card front">
    <div class="brand">
      <span class="brand-dot"></span>
      <span class="brand-name">Bramwell HVAC</span>
    </div>
    <div class="social" aria-label="Social links">
      <span></span><span></span><span></span>
    </div>
    <div class="person">
      <p class="person-name">Lonnie Tadwick</p>
      <p class="person-role">Owner</p>
    </div>
    <ul class="contact">
      <li>
        <svg viewBox="0 0 24 24" aria-hidden="true"><path d="M6.6 10.8a15.5 15.5 0 0 0 6.6 6.6l2.2-2.2c.3-.3.7-.4 1-.2 1.1.4 2.3.6 3.6.6.6 0 1 .4 1 1V20c0 .6-.4 1-1 1A17 17 0 0 1 3 4c0-.6.4-1 1-1h3.5c.6 0 1 .4 1 1 0 1.3.2 2.5.6 3.6.1.3 0 .7-.2 1z"/></svg>
        (970) 347-6159
      </li>
      <li>
        <svg viewBox="0 0 24 24" aria-hidden="true"><path d="M2 5h20v14H2z M2 5l10 8 10-8" fill="none" stroke="#d8262f" stroke-width="2.5"/></svg>
        office@bramwellhvac.com
      </li>
    </ul>
    <p class="address">P.O. Box 482, Dunmore, CO 80634</p>
  </section>

  <section class="card card-back" aria-label="Business card back">
    <div class="back-mark" role="img" aria-label="Large faint brand mark area"></div>
    <div class="back-title">
      <p class="line1">Bramwell HVAC</p>
      <p class="line2"><span class="rule"></span>Service LLC</p>
    </div>
  </section>
</body>
</html>
```